New Public Cloud Consulting Needs Powerpoint Template

Setting up a new consulting practice and need a powerpoint template and design that reflects our vision. We focus on KRT Public Cloud only. We want to emphasize innovation, cloud, speed. We are based in Asia, with headquarters in Singapore. We serve Asia and Europe customers. The attached file is the current template and logo that we use. However it is not dynamic enough. Blue is the color of our logo - but we must have other colors that complement the blue.

Target Market(s)

Innovation, cloud, advisory

Font styles to use
Other font styles liked:
• We want a different font that what is included in the file.

Requirements
Must have
• Logo which is included in the sample template and blue color - however we want other colors included. To date - most of the designs are completely blue - which we do not want. Additionally we need to create an image of innovation, future vision. Please do not include a picture of a cloud. That is not innovative.
Nice to have
• Would be nice to show people in some of the slides - professional etc. There is one slide in the attached presentation that gives you an idea of this concept. How else can we do this ?

```html
<!DOCTYPE html>
<html lang="en">
<head>
<meta charset="UTF-8">
<title>Cloud &amp; Digital Transformation</title>
<link href="https://fonts.googleapis.com/css2?family=Roboto:wght@400;500;700&display=swap" rel="stylesheet">
<style>
  :root {
    --paper: #ffffff;
    --headline-blue: #2b63c8;
    --ink-navy: #1c2a4e;
    --band-navy: #213766;
    --band-steel: #8fa1c4;
    --accent-amber: #f2a33a;
    --accent-coral: #ee6a4c;
    --accent-teal: #2fc4b2;
    --night-deep: #06123a;
    --night-mid: #0c2d7c;
    --night-violet: #3a2a84;
    --glow-cyan: #38d0f2;
    --city-amber: #f0a040;
  }
  * { margin: 0; padding: 0; box-sizing: border-box; }
  html, body {
    width: 1200px;
    height: 675px;
    overflow: hidden;
    background: var(--paper);
  }
  .slide {
    position: relative;
    width: 1200px;
    height: 675px;
    overflow: hidden;
    background: var(--paper);
    font-family: "Roboto", Arial, sans-serif;
  }
  .slide-art {
    position: absolute;
    inset: 0;
    width: 1200px;
    height: 675px;
  }
  .brand {
    position: absolute;
    left: 114px;
    top: 100px;
    display: flex;
    align-items: center;
    gap: 10px;
  }
  .brand-mark {
    width: 26px;
    height: 26px;
    background: var(--accent-amber);
  }
  .brand-name {
    font-size: 22px;
    font-weight: 500;
    color: var(--ink-navy);
    letter-spacing: 0.2px;
  }
  .headline {
    position: absolute;
    left: 116px;
    top: 252px;
    font-size: 56px;
    line-height: 66px;
    font-weight: 700;
    color: var(--headline-blue);
    letter-spacing: -0.4px;
    white-space: nowrap;
  }
  .tagline {
    position: absolute;
    left: 125px;
    top: 532px;
    font-size: 19px;
    font-weight: 400;
    color: var(--ink-navy);
  }
</style>
</head>
<body>
  <main class="slide">
    <svg class="slide-art" viewBox="0 0 1280 720" preserveAspectRatio="none">
      <defs>
        <linearGradient id="nightCity" x1="0" y1="0" x2="0.3" y2="1">
          <stop offset="0" stop-color="var(--night-deep)"/>
          <stop offset="0.4" stop-color="var(--night-mid)"/>
          <stop offset="0.7" stop-color="var(--night-violet)"/>
          <stop offset="1" stop-color="#2a2140"/>
        </linearGradient>
        <radialGradient id="cloudGlow" cx="0.78" cy="0.4" r="0.33">
          <stop offset="0" stop-color="var(--glow-cyan)" stop-opacity="0.85"/>
          <stop offset="0.6" stop-color="var(--accent-teal)" stop-opacity="0.25"/>
          <stop offset="1" stop-color="var(--accent-teal)" stop-opacity="0"/>
        </radialGradient>
        <radialGradient id="cityGlow" cx="0.82" cy="0.95" r="0.42">
          <stop offset="0" stop-color="var(--city-amber)" stop-opacity="0.75"/>
          <stop offset="0.5" stop-color="var(--accent-coral)" stop-opacity="0.3"/>
          <stop offset="1" stop-color="var(--accent-coral)" stop-opacity="0"/>
        </radialGradient>
        <linearGradient id="warmBand" x1="0" y1="0" x2="1" y2="1">
          <stop offset="0" stop-color="var(--accent-amber)"/>
          <stop offset="1" stop-color="var(--accent-coral)"/>
        </linearGradient>
      </defs>

      <g class="hero-photo" role="img" aria-label="Night city skyline from high above, with a glowing network cloud sending streams of light down into the buildings">
        <polygon points="385,0 1280,0 1280,720 965,720" fill="url(#nightCity)"/>
        <polygon points="385,0 1280,0 1280,720 965,720" fill="url(#cloudGlow)"/>
        <polygon points="385,0 1280,0 1280,720 965,720" fill="url(#cityGlow)"/>
      </g>

      <polygon class="band band-steel" points="310,0 350,0 570,228 500,228" fill="var(--band-steel)"/>
      <polygon class="band band-navy" points="350,0 385,0 522,165 482,165" fill="var(--band-navy)"/>
      <polygon class="band band-warm" points="800,550 860,550 1000,720 935,720" fill="url(#warmBand)"/>
    </svg>

    <div class="brand">
      <span class="brand-mark"></span>
      <span class="brand-name">Orbit Consulting Group</span>
    </div>

    <h1 class="headline">Everyone<br>Talks about<br>Cloud &amp; Digital<br>Transformation</h1>
    <p class="tagline">We do it differently</p>
  </main>
</body>
</html>
```